Modern home page design for a Dental Surgery

- This design will have a 5 day deadline only.

- The design must be based around the attached HPID (home page information design) called LUMA HPID. I've attached Word and PDF versions - these are the same. The table boxes are just for approximate placement of information – you DON'T have to make it look exactly like this. All fonts used in the HPID are only examples - you can use any Google font you wish.

- Information only is in orange text. Copy to go on the design in black text. Some instructions are in the HPID. Please be creative!

- The design needs to be modern. Colours are to be black and white with grey and blue like the logo colours. Background white please.

- I've provided the images for the galleries - they are labelled and will match the name in the HPID.

- I've provided icons for the items below the gallery - the name of the image will match the subheading for each section. You can use other icons if you want to.

- This is a website that is an example of what we like. Please DON'T copy this exactly though!
http://brightmolarclinic.example.co.nz/

Width of content will be 1100 pixels when implemented as a web page. Header height (without nav bar) 150-160 pixels.

If your design is chosen the winning PSD file will have to be provided as follows…
1. Canvas size of 2000px x 2000px - 72ppi in Adobe Photoshop (CS5 compatible)
2. Width of content section is 1100px wide - centered in the canvas
3. Any button rollovers/hovers in the PSD as hidden layers.
4. All fonts used must be Google fonts (except for the fonts in the header at the top of the page).
5. You will need to supply the chosen home page plus one example page (example page as a style guide for how all other pages will look). Example page is only the header and navigational bar at the top, an empty sector in the middle with a column (180 px wide) which can be left or right aligned which means the main sector is 920 pixels wide, and then the footer at the bottom of the page
Updates

Hi Designers, The 1st posted deadline for this project was incorrect; please note new deadline for November 22.

Target Market(s)

all ages that need dental care

Industry/Entity Type

Dental

Number of Pages Required

1 page

Font styles to use
Sans Serif

Requirements
Must have
• modern clean design - as per the Project Description
Should not have
• should not be cluttered. Just because I use tables to show information placement on the HPID - you do NOT have to use boxes around information in the design.

```html
<!DOCTYPE html>
<html lang="en">
<head>
<meta charset="utf-8">
<title>Family Dentistry Kerrow Bay</title>
<link href="https://fonts.googleapis.com/css2?family=Arimo:ital,wght@0,400;0,700;1,400&family=Roboto+Slab:wght@400&family=Roboto+Condensed:wght@400&display=swap" rel="stylesheet">
<style>
:root{
  --blue:#0d4a86;
  --blue-bright:#1f8fd6;
  --ink:#333;
  --grey-text:#666;
  --line:#d8d8d8;
  --footer:#5f5f5d;
  --page:#f7f7f7;
  --white:#fff;
}
*{margin:0;padding:0;box-sizing:border-box}
html,body{width:839px;height:1200px;overflow:hidden}
body{position:relative;background:var(--page);font-family:Arimo,Arial,sans-serif;color:var(--ink)}
.abs{position:absolute}
.site-header{left:0;top:0;width:839px;height:116px;background:var(--white)}
.brand{left:92px;top:30px;display:flex;align-items:center;gap:8px;font-family:Arimo,sans-serif;font-size:17px;color:var(--blue);font-weight:700}
.brand-dot{width:30px;height:30px;border-radius:50%;background:var(--blue)}
.tagline{left:356px;top:42px;font-size:17px;color:#555;line-height:19px}
.tagline strong{display:block;color:var(--blue);font-weight:400}
.phone{left:591px;top:47px;display:flex;gap:4px;align-items:center}
.phone small{display:block;font-size:8px;color:#444}
.phone b{display:block;font-size:16px;font-weight:400;color:var(--blue);line-height:16px}
.main-nav{left:0;top:116px;width:839px;height:25px;background:var(--blue);display:flex;padding-left:90px}
.main-nav a{color:var(--white);font-size:10px;text-decoration:none;line-height:25px;padding:0 13.5px}
.main-nav a.current{background:#e5e5e5;color:var(--ink);padding:0 18px}
.hero{left:0;top:141px;width:839px;height:247px;background:linear-gradient(135deg,#e7eaee 0%,#c9ced5 45%,#8d97a6 70%,#d9dde2 100%)}
.hero-caption{left:128px;top:233px;width:284px;height:61px;background:rgba(90,90,90,.75);color:var(--white);font-family:"Roboto Slab",serif;font-size:19px;line-height:24px;padding:6px 21px}
.arrow{width:32px;height:32px;border-radius:50%;background:var(--blue);top:248px;display:flex;align-items:center;justify-content:center}
.feature{top:414px;width:321px;height:136px;background:var(--blue);color:var(--white);padding:14px 14px;box-shadow:0 6px 6px -4px rgba(0,0,0,.35)}
.feature h2{font-family:"Roboto Slab",serif;font-weight:400;font-size:19px;margin-bottom:6px}
.feature p{font-size:8.6px;line-height:13px;width:200px}
.feature .icon-ring{position:absolute;right:19px;top:22px;width:68px;height:68px;border-radius:50%;background:var(--white);border:3px solid #b9c7d6;display:flex;align-items:center;justify-content:center}
.tag-btn{display:inline-block;position:relative;background:var(--blue-bright);color:var(--white);font-size:10px;font-weight:700;height:21px;line-height:21px;padding:0 16px;margin-top:10px}
.tag-btn::after{content:"";position:absolute;right:-9px;top:0;border-left:9px solid var(--blue-bright);border-top:10.5px solid transparent;border-bottom:10.5px solid transparent}
.info-box{top:569px;width:210px;height:133px;background:var(--white);border:1px solid var(--line);padding:10px 12px}
.info-box header{display:flex;gap:8px;align-items:flex-start}
.info-box h3{font-family:"Roboto Slab",serif;font-weight:400;font-size:13px;line-height:14px;color:var(--blue-bright)}
.info-box p{font-size:7.6px;line-height:13px;color:var(--grey-text);margin-top:10px}
.info-box .tag-btn{font-size:9px;padding:0 10px;margin-top:8px}
.emergency{left:90px;top:721px;width:655px;height:72px;background:var(--white);border:1px solid var(--line);display:flex;gap:10px;padding:8px 10px}
.emergency h3{font-family:"Roboto Slab",serif;font-weight:400;font-size:15px;margin-top:2px}
.associations{left:90px;top:813px;width:348px;height:96px;background:var(--white);border:1px solid var(--line);padding:8px 10px}
.associations h3{font-family:"Roboto Slab",serif;font-weight:400;font-size:16px}
.associations p{font-size:7.6px;font-style:italic;color:var(--grey-text);line-height:11px;width:110px;margin-top:8px}
.badge-a{left:138px;top:34px;width:76px;height:42px;background:#e8e8e8;border-radius:3px}
.badge-b{left:242px;top:28px;width:80px;height:52px;border-radius:50%;background:#0e6b6e}
.testimonial{left:451px;top:813px;width:294px;height:96px;background:var(--white);border:1px solid var(--line)}
.portrait{left:13px;top:16px;width:78px;height:68px;background:linear-gradient(#c6cdd5,#7d8a99)}
.quote{left:125px;top:10px;width:156px;font-size:7.2px;line-height:10.5px;font-style:italic;color:var(--grey-text)}
.quote-mark{font-family:Georgia,serif;color:#bbb;font-size:22px}
.cite{left:126px;top:77px;font-size:8px;font-weight:700;color:var(--ink)}
.site-footer{left:0;top:947px;width:839px;height:225px;background:var(--footer);color:var(--white)}
.site-footer h4{font-family:"Roboto Condensed",sans-serif;font-weight:400;font-size:13px;position:absolute;top:15px}
.f-col{position:absolute;top:42px;font-size:8px;line-height:13px}
.f-col li{list-style:none}
.f-col li.gap{margin-top:4px}
.f-col li.sub{padding-left:12px}
.f-col li.sub::before{content:"› ";}
.f-rule{position:absolute;top:28px;width:1px;height:180px;background:#777}
.copyright{left:0;top:1172px;width:839px;height:28px;background:var(--blue);color:var(--white);font-size:8px;text-align:center;line-height:28px}
</style>
</head>
<body>
<header class="site-header abs">
  <div class="brand abs"><span class="brand-dot"></span>Lumen Dental Group</div>
  <div class="tagline abs">Family Dentistry<strong>KERROW BAY</strong></div>
  <div class="phone abs">
    <svg width="20" height="20" viewBox="0 0 20 20"><circle cx="10" cy="10" r="9" fill="none" stroke="#555" stroke-width="1"/><path d="M7 5c-1 1-1 3 0 5s3 5 6 5l1-2-2-1-1 1c-1-1-2-2-3-4l1-1-1-2z" fill="#555"/></svg>
    <div><small>Call Us Today</small><b>04 555 0192</b></div>
  </div>
</header>
<nav class="main-nav abs">
  <a class="current" href="#">HOME</a><a href="#">ABOUT</a><a href="#">WHAT WE DO</a><a href="#">WHY CHOOSE US</a><a href="#">SERVICES</a><a href="#">COSTS</a><a href="#">APPOINTMENT</a><a href="#">CONTACT/MAP</a>
</nav>
<div class="hero abs" role="img" aria-label="Bright dental surgery room with a blue patient chair, cabinets and a snowy window"></div>
<div class="hero-caption abs">Your local dental surgery<br>Ashdene &amp; Kerrow Bay</div>
<div class="arrow abs" style="left:78px"><svg width="12" height="12" viewBox="0 0 12 12"><path d="M8 1 3 6l5 5" fill="none" stroke="#fff" stroke-width="2.4"/></svg></div>
<div class="arrow abs" style="left:726px"><svg width="12" height="12" viewBox="0 0 12 12"><path d="M4 1l5 5-5 5" fill="none" stroke="#fff" stroke-width="2.4"/></svg></div>

<section class="feature abs" style="left:90px">
  <h2>What We Do</h2>
  <p>The Lumen Dental Centre offer a wide range of dental services including diagnostics, orthodontics, dentures, oral surgery, and periodontal, root canal and cosmetic dentistry.</p>
  <a class="tag-btn" href="#">MORE</a>
  <div class="icon-ring"><svg width="30" height="36" viewBox="0 0 30 36"><path d="M8 3c3 0 4 2 7 2s4-2 7-2c4 0 5 4 4 8l-3 10c-1 3-3 3-3 0l-2-6-3 6c-1 3-3 3-3 0L7 11C6 7 5 3 8 3z" fill="none" stroke="#0d4a86" stroke-width="2"/><path d="M15 20v8c0 4 6 4 6 0" fill="none" stroke="#0d4a86" stroke-width="2"/><circle cx="22" cy="31" r="2" fill="#1f8fd6"/></svg></div>
</section>
<section class="feature abs" style="left:424px">
  <h2>How much does it Cost?</h2>
  <p>Find out estimates of how much each dental procedure costs. (Exact prices will be discussed with you after consultation depending on your specific dental requirements.)</p>
  <a class="tag-btn" href="#">COSTS</a>
  <div class="icon-ring"><svg width="30" height="36" viewBox="0 0 30 36"><path d="M8 3c3 0 4 2 7 2s4-2 7-2c4 0 5 4 4 8l-3 16c-1 3-3 3-3 0l-2-8-3 8c-1 3-3 3-3 0L7 11C6 7 5 3 8 3z" fill="none" stroke="#0d4a86" stroke-width="2"/><path d="M10 12l4 4 7-8" fill="none" stroke="#1f8fd6" stroke-width="2.2"/></svg></div>
</section>

<section class="info-box abs" style="left:90px">
  <header><svg width="32" height="28" viewBox="0 0 32 28"><path d="M2 24l8-4 18-14" fill="none" stroke="#0d4a86" stroke-width="3"/><path d="M6 14l8 4" stroke="#1f8fd6" stroke-width="2"/></svg><h3>Make an<br>Appointment</h3></header>
  <p>Two convenient locations in Ashdene and Kerrow Bay offer dental services for all ages. Take a moment to book your appointment</p>
  <a class="tag-btn" href="#">APPOINTMENT</a>
</section>
<section class="info-box abs" style="left:313px">
  <header><svg width="26" height="30" viewBox="0 0 26 30"><path d="M6 3c3 0 4 2 7 2s4-2 7-2c4 0 4 4 3 8l-3 14c-1 3-3 3-3 0l-2-7-2 7c-1 3-3 3-3 0L3 11C2 7 2 3 6 3z" fill="none" stroke="#0d4a86" stroke-width="1.8"/></svg><h3>Your First<br>Consultation</h3></header>
  <p>Want to know what will happen in your first consultation? Check out our first dental consultation process.</p>
  <a class="tag-btn" href="#">1 CONSULTATION</a>
</section>
<section class="info-box abs" style="left:535px">
  <header><svg width="26" height="30" viewBox="0 0 26 30"><rect x="4" y="4" width="18" height="23" rx="2" fill="none" stroke="#0d4a86" stroke-width="2"/><rect x="9" y="2" width="8" height="4" fill="#1f8fd6"/><path d="M8 13h10M8 17h10M8 21h7" stroke="#0d4a86" stroke-width="1.5"/></svg><h3>Application<br>Form</h3></header>
  <p>Save time and fill in an online application form (or download, print out and complete) before your first visit.</p>
  <a class="tag-btn" href="#">APPLICATION</a>
</section>

<section class="emergency abs">
  <svg width="30" height="56" viewBox="0 0 30 56"><path d="M7 4c3 0 5 2 8 2s5-2 8-2c5 0 5 6 4 12l-4 22c-1 4-3 4-4 0l-4-12-4 12c-1 4-3 4-4 0L3 16C2 10 2 4 7 4z" fill="none" stroke="#0d4a86" stroke-width="2"/></svg>
  <h3>Is this an Emergency?</h3>
</section>

<section class="associations abs">
  <h3>Associations</h3>
  <p>Lorem ipsum dolor sit amet, consectetuer adipiscing elit, sed diam nonummy.</p>
  <div class="badge-a abs"></div>
  <div class="badge-b abs"></div>
</section>
<section class="testimonial abs">
  <div class="portrait abs" role="img" aria-label="Portrait photo of a smiling patient"></div>
  <span class="quote-mark abs" style="left:100px;top:4px">“</span>
  <p class="quote abs">Lorem ipsum dolor sit amet, consectetuer adipiscing elit, sed diam nonummy nibh tincidunt ut laoreet dolore magna aliquam volutpat. Ut wisi enim ad minim veniam, nostrud exerci tation ullamcorper nisl ut ex ea commodo consequat.</p>
  <span class="cite abs">Your Name, Title</span>
  <span class="quote-mark abs" style="left:218px;top:70px">”</span>
  <svg class="abs" style="left:262px;top:77px" width="14" height="14" viewBox="0 0 14 14"><circle cx="7" cy="7" r="6" fill="none" stroke="#ccc"/><path d="M6 4l3 3-3 3" fill="none" stroke="#ccc"/></svg>
</section>

<footer class="site-footer abs">
  <h4 style="left:93px">Quick Links</h4>
  <h4 style="left:200px">Services</h4>
  <div class="f-rule" style="left:187px"></div>
  <div class="f-rule" style="left:376px"></div>
  <div class="f-rule" style="left:590px"></div>
  <ul class="f-col" style="left:93px">
    <li>Home</li><li class="gap">About</li><li class="sub">Team</li><li class="sub">Registration form</li><li class="gap">What We Do</li><li class="gap">Why Choose Us</li><li class="sub">Testimonials</li><li class="gap">Costs</li><li class="gap">Appointment</li><li class="gap">Contact / Map</li>
  </ul>
  <ul class="f-col" style="left:202px">
    <li>Restorative Dentistry</li><li class="gap">Preventative</li><li class="sub">Fissure Sealants</li><li class="sub">Mouthguards</li><li class="sub">Bite Splints</li><li class="gap">Fillings</li><li class="sub">Amalgams, Composites (white fillings)</li><li class="sub">Porcelain &amp; Gold</li><li class="gap">Crown &amp; Bridge Treatment</li><li class="gap">Implants</li>
  </ul>
  <ul class="f-col" style="left:390px">
    <li>Oral Surgery</li><li class="sub">Extractions</li><li class="sub">Minor Impacted Wisdom Teeth</li><li class="gap">Periodontal (gum) Care</li><li class="sub">Hygiene Services</li><li class="sub">Minor Periodontal Surgery</li><li class="sub">Preventative Services</li><li class="gap">Root Canal Therapy</li><li class="gap">Cosmetic</li><li class="sub">Porcelain Veneers</li><li class="sub">Glow Bleaching (in surgery teeth whitening)</li><li class="gap">Dentures</li>
  </ul>
  <ul class="f-col" style="left:605px">
    <li>Orthodontics</li><li class="gap">Children &amp; pre-schoolers</li><li class="sub">Free Secondary School Dentistry</li><li class="sub">Free Dental Care Under 18</li><li class="sub">Pre-school Dentistry</li><li class="gap">Oral Care Products</li><li class="gap">Diagnostic Dentistry</li><li class="sub">Digital X-rays</li><li class="sub">Panoramic X-rays</li><li class="sub">Intra-oral photography &amp; Camera</li><li class="sub">Laser Cavity Detection</li>
  </ul>
</footer>
<div class="copyright abs">Copyright ©2014 Lumen Group. All Rights Reserved</div>
</body>
</html>
```